Neuaufbereitung Illustration
Zielgruppe
Wir beraten Unternehmen hinsichtlich einer ethischen und funktional umfassenden Corporate Governance sowie Unternehmensführung inklusive einer individuellen Erfolgsgeschichte. Wir sorgen für einen wertvollen Auftritt.
Führungskräfte: Geschäftsleitungs- und Verwaltungsrats-Mitglieder.
Aufgabenstellung
Überarbeitung der Grafik im Anhang in Abstimmung mit dem Grundauftritt und -Design von finewerk (siehe: www.finewerk.eu)
Bitte für Bild-Legende und Detailbezeichnung Datei "finewerk sketch 04 182" beiziehen!

```html
<!DOCTYPE html>
<html lang="de">
<head>
<meta charset="utf-8">
<title>Besser sein dank einer Ideologisierung</title>
<link rel="stylesheet" href="https://fonts.googleapis.com/css2?family=Roboto:wght@500;700;900&display=swap">
<style>
  :root{
    --bg:#e9e9e9;
    --paper:#ffffff;
    --brown:#786843;
    --brown-text:#6a5a34;
    --grey:#cfcfcf;
    --grey-dark:#8a8a8a;
    --icon-grey:#9c9c9c;
    --icon-light:#d9d9d9;
  }
  html,body{margin:0;padding:0;width:1200px;height:1200px;overflow:hidden;background:var(--bg);}
  .sheet{position:absolute;left:0;top:290px;width:1200px;height:620px;background:var(--paper);box-shadow:0 10px 30px rgba(0,0,0,.12);}
  .sheet svg{display:block;width:1200px;height:620px;font-family:'Roboto',Arial,sans-serif;}
  .title-main{fill:#fff;font-weight:900;font-size:58px;}
  .title-sub{fill:var(--brown-text);font-weight:700;font-size:34px;}
  .tag-text{fill:#fff;font-weight:700;font-size:22px;}
  .quote{fill:var(--brown-text);font-weight:700;font-size:12px;}
  .node-label{fill:var(--brown-text);font-weight:700;font-size:14px;}
  .era-year{fill:#fff;font-weight:700;font-size:34px;}
  .era-name{fill:#fff;font-weight:700;font-size:18px;}
  .benefit{fill:var(--brown-text);font-weight:700;font-size:14px;}
  .benefit-tag{fill:var(--brown-text);font-weight:700;font-size:13px;}
  .arrow{stroke:var(--brown);stroke-width:1.4;fill:none;marker-end:url(#head);}
  .arrow-both{stroke:var(--brown);stroke-width:1.4;fill:none;marker-end:url(#head);marker-start:url(#tail);}
  .timeline{stroke:var(--brown);stroke-width:6;stroke-dasharray:26 18;}
</style>
</head>
<body>
<div class="sheet">
<svg viewBox="0 0 1200 620" xmlns="http://www.w3.org/2000/svg">
  <defs>
    <marker id="head" markerWidth="8" markerHeight="8" refX="7" refY="4" orient="auto"><path d="M0,0 L8,4 L0,8 Z" fill="#786843"/></marker>
    <marker id="tail" markerWidth="8" markerHeight="8" refX="1" refY="4" orient="auto"><path d="M8,0 L0,4 L8,8 Z" fill="#786843"/></marker>
    <g id="truck">
      <rect x="0" y="0" width="36" height="24" fill="#c4c4c4"/>
      <path d="M36,6 h12 l8,10 v8 h-20 Z" fill="#9c9c9c"/>
      <circle cx="10" cy="26" r="5" fill="#333"/><circle cx="46" cy="26" r="5" fill="#333"/>
    </g>
    <g id="house">
      <path d="M0,24 L26,0 L52,24 Z" fill="#cfcfcf"/>
      <rect x="6" y="24" width="40" height="28" fill="#e0e0e0"/>
      <rect x="20" y="32" width="12" height="20" fill="#777"/>
      <rect x="-4" y="52" width="60" height="4" fill="#786843"/>
    </g>
    <g id="case">
      <rect x="14" y="0" width="16" height="8" rx="2" fill="none" stroke="#9c9c9c" stroke-width="3"/>
      <rect x="0" y="6" width="44" height="28" rx="3" fill="#c9c9c9"/>
      <rect x="0" y="16" width="44" height="3" fill="#9c9c9c"/>
    </g>
    <g id="chart">
      <path d="M0,0 V36 H40" stroke="#9c9c9c" stroke-width="3" fill="none"/>
      <path d="M6,30 L16,18 L24,24 L36,8" stroke="#786843" stroke-width="4" fill="none"/>
      <path d="M30,6 L38,6 L38,14 Z" fill="#786843"/>
    </g>
    <g id="hex"><path d="M-32,0 L-18,-28 H18 L32,0 L18,28 H-18 Z" fill="#786843"/></g>
    <g id="tick">
      <path d="M0,6 L6,12 L16,0" stroke="#786843" stroke-width="4" fill="none" stroke-linecap="round" stroke-linejoin="round"/>
    </g>
  </defs>

  <!-- Title -->
  <path d="M530,60 H1140 L1170,105 L1140,150 H490 Z" fill="var(--grey)"/>
  <text class="title-sub" x="560" y="118">DANK EINER IDEOLOGISIERUNG</text>
  <path d="M70,30 H470 L510,80 L470,130 H70 L40,80 Z" fill="var(--brown)"/>
  <text class="title-main" x="100" y="102">BESSER SEIN</text>

  <!-- Funktion -->
  <path d="M0,112 H150 L165,132 L150,152 H0 Z" fill="var(--brown)"/>
  <text class="tag-text" x="20" y="140">FUNKTION</text>
  <text class="quote" x="90" y="185" text-anchor="middle">„NUR MITTEL ZUM</text>
  <text class="quote" x="90" y="200" text-anchor="middle">ZWECK GEDANKEN“</text>

  <!-- Linear model -->
  <rect x="286" y="162" width="28" height="36" rx="6" fill="var(--icon-light)" role="img" aria-label="Symbolfigur Mitarbeiter"/>
  <text class="node-label" x="300" y="218" text-anchor="middle">MITARBEITER</text>
  <use href="#truck" x="274" y="232"/>
  <text class="node-label" x="300" y="282" text-anchor="middle">LIEFERANTEN</text>
  <use href="#chart" x="282" y="296"/>
  <text class="node-label" x="300" y="350" text-anchor="middle">INVESTOREN</text>
  <use href="#house" x="410" y="240"/>
  <text class="node-label" x="436" y="318" text-anchor="middle">UNTERNEHMEN</text>
  <use href="#case" x="548" y="262"/>
  <text class="node-label" x="570" y="318" text-anchor="middle">KUNDEN</text>
  <path class="arrow" d="M348,200 L398,246"/>
  <path class="arrow" d="M340,252 L398,258"/>
  <path class="arrow" d="M340,316 L398,274"/>
  <path class="arrow" d="M472,278 L530,280"/>

  <!-- Cooperation model -->
  <text class="node-label" x="700" y="200" text-anchor="middle">LIEFERANTEN</text>
  <use href="#truck" x="672" y="210"/>
  <text class="node-label" x="935" y="222" text-anchor="middle">KUNDEN</text>
  <use href="#case" x="912" y="232"/>
  <use href="#house" x="790" y="250"/>
  <text class="node-label" x="816" y="326" text-anchor="middle">UNTERNEHMEN</text>
  <rect x="688" y="300" width="28" height="36" rx="6" fill="var(--icon-light)" role="img" aria-label="Symbolfigur Mitarbeiter"/>
  <text class="node-label" x="702" y="353" text-anchor="middle">MITARBEITER</text>
  <use href="#chart" x="902" y="330"/>
  <text class="node-label" x="922" y="388" text-anchor="middle">INVESTOREN</text>
  <path class="arrow-both" d="M742,222 Q820,206 900,236"/>
  <path class="arrow-both" d="M738,246 L784,272"/>
  <path class="arrow-both" d="M852,284 L904,262"/>
  <path class="arrow-both" d="M700,250 L700,292"/>
  <path class="arrow-both" d="M936,274 L930,322"/>
  <path class="arrow-both" d="M724,316 L784,294"/>
  <path class="arrow-both" d="M858,296 L900,330"/>
  <path class="arrow-both" d="M752,362 Q820,376 896,358"/>

  <!-- Kooperation -->
  <path d="M1020,236 H1200 V282 H1020 L1005,259 Z" fill="var(--brown)"/>
  <text class="tag-text" x="1040" y="267">KOOPERATION</text>
  <text class="quote" x="1100" y="305" text-anchor="middle">„MITTEL UND ZWECK</text>
  <text class="quote" x="1100" y="320" text-anchor="middle">GEDANKEN“</text>

  <!-- Timeline -->
  <line class="timeline" x1="150" y1="440" x2="1060" y2="440"/>
  <path d="M0,405 H140 L165,440 L140,475 H0 Z" fill="var(--brown)"/>
  <text class="era-year" x="25" y="453">1850</text>
  <path d="M1070,405 H1200 V475 H1070 L1045,440 Z" fill="var(--brown)"/>
  <text class="era-year" x="1080" y="453">JETZT</text>

  <!-- Industrialisierung -->
  <use href="#hex" x="260" y="440"/>
  <path d="M244,452 V428 h6 v8 l8,-6 v6 l8,-6 v6 l8,-6 v20 Z" fill="#fff"/>
  <path d="M260,474 H450 L470,497 L450,520 H260 Z" fill="var(--brown)"/>
  <text class="era-name" x="272" y="504">INDUSTRIALISIERUNG</text>
  <use href="#tick" x="272" y="532"/><text class="benefit" x="298" y="545">GÜNSTIGER</text>
  <use href="#tick" x="272" y="558"/><text class="benefit" x="298" y="571">SCHNELLER</text>
  <path d="M262,582 H410 L420,594 L410,606 H262 Z" fill="var(--grey)"/>
  <text class="benefit-tag" x="280" y="599">PRODUKTNUTZEN</text>

  <!-- Technologisierung -->
  <use href="#hex" x="560" y="440"/>
  <rect x="550" y="422" width="20" height="36" rx="4" fill="none" stroke="#fff" stroke-width="3"/>
  <path d="M556,474 H760 L780,497 L760,520 H556 L545,497 Z" fill="var(--brown)"/>
  <text class="era-name" x="568" y="504">TECHNOLOGISIERUNG</text>
  <use href="#tick" x="568" y="532"/><text class="benefit" x="594" y="545">EINFACHER</text>
  <use href="#tick" x="568" y="558"/><text class="benefit" x="594" y="571">UMFASSENDER</text>
  <path d="M558,582 H710 L720,594 L710,606 H558 Z" fill="var(--grey)"/>
  <text class="benefit-tag" x="580" y="599">KUNDENNUTZEN</text>

  <!-- Ideologisierung -->
  <use href="#hex" x="810" y="440"/>
  <path d="M798,438 h6 v16 h-6 Z M806,438 l6,-14 c4,0 5,3 4,7 l-1,5 h8 c3,0 4,3 3,5 l-3,11 c-1,2 -2,3 -4,3 h-13 Z" fill="#fff"/>
  <path d="M806,474 H1000 L1020,497 L1000,520 H806 L795,497 Z" fill="var(--brown)"/>
  <text class="era-name" x="820" y="504">IDEOLOGISIERUNG</text>
  <use href="#tick" x="818" y="532"/><text class="benefit" x="844" y="545">SINNVOLLER</text>
  <use href="#tick" x="818" y="558"/><text class="benefit" x="844" y="571">WERTVOLLER</text>
  <path d="M808,582 H960 L970,594 L960,606 H808 Z" fill="var(--grey)"/>
  <text class="benefit-tag" x="828" y="599">GEMEINNUTZEN</text>
</svg>
</div>
</body>
</html>
```